Help me create an amazing cover for my first ebook!!

I am looking to have a modern and professional looking cover for my first ebook. It will be published through Borvex Quill Self Press and will need to follow their formatting and guidelines. I want the cover to have a modern and vibrant feel, that appeals to a millennial audience. This is a real estate book that is focused on a niche category catered to young professionals, so the idea would be to appeal to them.

Title:
The Twentysomething Playbook for Duplex Living

A Smart Property Buying Plan to Start Early, Cut Your Housing Costs (Sometimes to Zero), and Speed Up Your Path to Lasting Wealth.

Davin Osterlund

Target Market(s)

Real Estate investors, investors, millennials, young professionals, college educated, 20-40 years old.Financial freedom, finance.

Industry/Entity Type

Real Estate

Font styles to use
Sans Serif

Colors

Designer to choose colors to be used in the design.

Requirements
Must have
• Must follow the borvex quill self press format. I attached a screenshot of the details, it can also be found here: https://qsp.borvexbooks.example/en_US/help/topic/R481736025
• Must include this title:
• The Twentysomething Playbook for Duplex Living
• A Smart Property Buying Plan to Start Early, Cut Your Housing Costs (Sometimes to Zero), and Speed Up Your Path to Lasting Wealth.
• Davin Osterlund.
• I added examples of book covers I like to use as a guide, I also added some color pallette examples.
Nice to have
• Modern, clean design that's not too busy. Some sort of simple photo or illustration to incorporate in the cover along with the text would be nice.

```html
<!DOCTYPE html>
<html lang="en">
<head>
<meta charset="utf-8">
<title>The Twentysomething Playbook for Duplex Living — Davin Osterlund</title>
<link rel="stylesheet" href="https://fonts.googleapis.com/css2?family=Oranienbaum&display=swap">
<style>
  :root {
    --cover-red: #7e1529;
    --cover-red-deep: #660e20;
    --cover-red-light: #8c1e33;
    --paper-white: #f2f2f4;
    --ink-white: #ffffff;
    --art-grey: #d9d9dc;
    --art-gold: #c9c27a;
    --art-shadow: #8a2a3b;
  }
  * { margin: 0; padding: 0; box-sizing: border-box; }
  html, body {
    width: 750px;
    height: 1200px;
    overflow: hidden;
    background: var(--paper-white);
  }
  .cover {
    position: relative;
    width: 750px;
    height: 1200px;
    overflow: hidden;
    background: linear-gradient(180deg, var(--cover-red-light) 0%, var(--cover-red) 45%, var(--cover-red-deep) 100%);
    font-family: "Oranienbaum", "Times New Roman", serif;
    color: var(--ink-white);
    text-align: center;
  }
  .cover__curves {
    position: absolute;
    inset: 0;
    width: 750px;
    height: 1200px;
  }
  .cover__art {
    position: absolute;
    left: 100px;
    top: 70px;
    width: 590px;
    height: 470px;
  }
  .title {
    position: absolute;
    left: 0;
    right: 0;
    top: 565px;
    text-transform: uppercase;
    line-height: 1;
    text-shadow: 0 2px 3px rgba(0,0,0,0.25);
  }
  .title__main {
    display: block;
    font-size: 80px;
    letter-spacing: 0.5px;
  }
  .title__sub {
    display: block;
    margin-top: 10px;
    font-size: 54px;
    letter-spacing: 0.5px;
  }
  .subtitle {
    position: absolute;
    left: 40px;
    right: 40px;
    top: 788px;
    font-size: 27px;
    line-height: 1.3;
  }
  .subtitle__line { display: block; }
  .subtitle__highlight {
    display: inline-block;
    margin-top: 6px;
    padding: 2px 10px 4px;
    background: var(--paper-white);
    color: var(--cover-red);
    outline: 2px dashed var(--cover-red);
    outline-offset: -5px;
    font-size: 30px;
  }
  .author {
    position: absolute;
    left: 0;
    right: 0;
    top: 1002px;
    font-size: 50px;
    text-transform: uppercase;
    letter-spacing: 0.5px;
  }
  .author__flourish {
    position: absolute;
    left: 255px;
    top: 1068px;
    width: 240px;
    height: 30px;
  }
</style>
</head>
<body>
  <main class="cover">
    <svg class="cover__curves" viewBox="0 0 750 1200" aria-hidden="true">
      <path d="M330 0 Q520 95 750 45 L750 0 Z" fill="var(--paper-white)"/>
      <path d="M0 1200 L0 1175 Q375 1080 750 1175 L750 1200 Z" fill="var(--paper-white)"/>
    </svg>

    <svg class="cover__art" viewBox="0 0 590 470" role="img" aria-label="Illustration of a blank white figure in a tie pointing at a modern two-storey house with a grey roof and yellow walls">
      <defs>
        <linearGradient id="artTone" x1="0" y1="0" x2="1" y2="1">
          <stop offset="0" stop-color="var(--art-grey)"/>
          <stop offset="0.6" stop-color="var(--art-gold)"/>
          <stop offset="1" stop-color="var(--art-shadow)"/>
        </linearGradient>
      </defs>
      <rect x="0" y="0" width="590" height="470" rx="18" fill="url(#artTone)" opacity="0.85"/>
    </svg>

    <h1 class="title">
      <span class="title__main">The Twentysomething</span>
      <span class="title__sub">Playbook for Duplex Living</span>
    </h1>

    <p class="subtitle">
      <span class="subtitle__line">A Smart Property Buying Plan to Start Early, Cut Your</span>
      <span class="subtitle__line">Housing Costs (Sometimes to Zero), and Speed Up</span>
      <span class="subtitle__highlight">Your Path to Lasting Wealth</span>
    </p>

    <p class="author">Davin Osterlund</p>

    <svg class="author__flourish" viewBox="0 0 240 30" role="img" aria-label="Decorative scroll flourish">
      <rect x="0" y="8" width="240" height="14" rx="7" fill="var(--ink-white)" opacity="0.85"/>
    </svg>
  </main>
</body>
</html>
```